Screendesign für neue Website
Zielgruppe
Bauherren und alle die mal zum Architekten müssen.
Aufgabenstellung
Bei diesem Auftrag handelt es sich um die Erstellung eines Screendesigns für eine Website eines Archtiktenbüros.
Es wird daher ein Layout im PSD-Format erwartet, eine Umsetzung dessen in HTML wird nicht gefordert.

```html
<!DOCTYPE html>
<html lang="de">
<head>
<meta charset="utf-8">
<title>Planungsbüro Lorenz Wiebe</title>
<link href="https://fonts.googleapis.com/css2?family=Source+Sans+3:wght@400;600;700&display=swap" rel="stylesheet">
<style>
:root{
  --bg-top:#3a3a3a;
  --bg-bottom:#232323;
  --frame:#4a4a4a;
  --panel-light:#ffffff;
  --panel-dark:#dcdcdc;
  --nav:#383838;
  --nav-active:#6b6b6b;
  --nav-text:#d8d8d8;
  --text-strong:#757575;
  --text-mid:#8a8a8a;
  --text-light:#b0b0b0;
  --rule:#8c8c8c;
  --white:#ffffff;
  --photo-edge:#8fb56a;
}
*{margin:0;padding:0;box-sizing:border-box}
html,body{width:1200px;height:960px;overflow:hidden}
body{
  position:relative;
  font-family:"Source Sans 3",sans-serif;
  background:linear-gradient(180deg,var(--bg-top) 0,#2c2c2c 260px,var(--bg-bottom) 960px);
}
.site-title{position:absolute;left:82px;top:68px;color:var(--white);font-size:14px;font-weight:600}
.frame{position:absolute;left:63px;top:99px;width:1077px;height:609px;background:var(--frame);border-radius:6px}
.panel{position:absolute;left:70px;top:108px;width:1062px;height:592px;
  background:linear-gradient(180deg,var(--panel-light) 0,#f2f2f2 40%,var(--panel-dark) 100%)}
.gallery{position:absolute;left:81px;top:117px;display:flex;gap:3px}
.photo{width:171px;height:168px;border:2px solid var(--photo-edge);border-top:0;
  background:linear-gradient(180deg,#7fa8d8 0,#c9d9ea 35%,#b9a590 60%,#9fbf86 100%)}
.photo.warm{background:linear-gradient(180deg,#6a95c9 0,#8a4a6a 35%,#e0b060 60%,#a0a8a0 100%)}
.arrow{position:absolute;top:188px;width:25px;height:25px}
.arrow.prev{left:58px}.arrow.next{left:1117px}
.nav{position:absolute;left:777px;top:288px;width:170px;list-style:none}
.nav li{height:52.5px;line-height:52px;text-align:center;background:var(--nav);color:var(--nav-text);
  font-size:14px;border-bottom:1px solid #555}
.nav li.active{background:var(--nav-active);color:var(--white);font-weight:600}
.nav-caret{position:absolute;left:850px;top:611px}
.claim{position:absolute;color:var(--text-mid);white-space:nowrap;line-height:1}
.quote{position:absolute;font-size:110px;color:#c4c4c4;font-style:italic;line-height:1}
.rule{position:absolute;left:147px;top:576px;width:582px;height:1px;background:var(--rule)}
.welcome{position:absolute;right:471px;top:585px;font-size:13.5px;font-weight:700;color:#444}
.footer-links{position:absolute;right:78px;top:721px;color:var(--white);font-size:13.5px;font-weight:600}
.brand{position:absolute;left:72px;top:760px;display:flex;align-items:center;gap:10px;color:var(--white);font-size:22px;font-weight:700}
.brand span.mark{width:26px;height:26px;background:var(--white)}
</style>
</head>
<body>
<div class="site-title">Planungsbüro Lorenz Wiebe</div>
<div class="frame"></div>
<div class="panel"></div>

<div class="gallery">
  <div class="photo" role="img" aria-label="Foto: weißes Einfamilienhaus mit dunklem Dach"></div>
  <div class="photo" role="img" aria-label="Foto: helles Haus mit Wintergarten"></div>
  <div class="photo warm" role="img" aria-label="Foto: beleuchtetes Holzhaus am Abend"></div>
  <div class="photo" role="img" aria-label="Foto: weißes Einfamilienhaus mit dunklem Dach"></div>
  <div class="photo" role="img" aria-label="Foto: helles Haus mit Wintergarten"></div>
  <div class="photo warm" role="img" aria-label="Foto: beleuchtetes Holzhaus am Abend"></div>
</div>

<svg class="arrow prev" viewBox="0 0 25 25"><circle cx="12.5" cy="12.5" r="12" fill="#e8e8e8" stroke="#888"/><path d="M14.5 8 L9.5 12.5 L14.5 17Z" fill="#444"/></svg>
<svg class="arrow next" viewBox="0 0 25 25"><circle cx="12.5" cy="12.5" r="12" fill="#e8e8e8" stroke="#888"/><path d="M10.5 8 L15.5 12.5 L10.5 17Z" fill="#444"/></svg>

<ul class="nav">
  <li>Unternehmen</li>
  <li class="active">Projekte</li>
  <li>Information</li>
  <li>Aktuelles</li>
  <li>Leistungen</li>
  <li>Kontakt</li>
</ul>
<svg class="nav-caret" width="18" height="10" viewBox="0 0 18 10"><path d="M0 10 L9 1 L18 10Z" fill="#444"/></svg>

<div class="quote" style="left:145px;top:318px">“</div>
<div class="claim" style="left:190px;top:358px;font-size:40px">Architekten schaffen</div>
<div class="claim" style="left:388px;top:400px;font-size:38px;color:var(--text-light)">Lebens-Raum</div>
<div class="claim" style="left:250px;top:440px;font-size:34px">Lebens-Traum</div>
<div class="claim" style="left:338px;top:474px;font-size:68px;color:var(--text-strong)">Traum Haus.</div>
<div class="quote" style="left:700px;top:448px">“</div>

<div class="rule"></div>
<div class="welcome">Willkommen im Planungsbüro Lorenz Wiebe!</div>

<div class="footer-links">Kontakt &nbsp;|&nbsp; Impressum</div>
<div class="brand"><span class="mark"></span>Lorenz Wiebe</div>
</body>
</html>
```